We need motivational posters designed to be used in classrooms at a truck driving school. The purpose of the posters is to motivate the students.

I want the the quotes to be the main focal point of emphasis and our logo on the bottom of the poster for branding purposes.

I would like the images to be related to the trucking industry

Below are the quotes for the posters

Poster 1
"Start where you are. Use what you have. Do what you can."
-Delmar Quisby-

Poster 2
"The secret of getting ahead is getting started"
-Owen Farrow-

Poster 3
"Most effective way to do it, is to do it."
-Rosalind Pemberly-

Poster 4
"Set your goals big, and don't stop till you get there."
-Cy Whitlock-

Poster 5
"If you are not willing to learn, no one can help you. If you are determined to learn, no one can stop you."
-Unknown-

Poster 6
"The will to succeed is important, but what's more important is the will to prepare."
-Dougie Hallam-

THESE POSTERS SHOULD BE DESIGNED AS 18X24
LANDSCAPE AND PORTRAIT ORIENTATION

Industry/Entity Type

School

```html
<!DOCTYPE html>
<html lang="en">
<head>
<meta charset="utf-8">
<title>Truck Driving School Motivational Posters</title>
<link rel="stylesheet" href="https://fonts.googleapis.com/css2?family=Bebas+Neue&display=swap">
<style>
  :root {
    --page-bg: #ffffff;
    --quote-white: #ffffff;
    --brand-ink: #2a2a2a;
    --brand-dot: #e8b21c;
    --valley-top: #c7ccc2;
    --valley-mid: #a3ad98;
    --valley-low: #c4c6bd;
    --cliff-top: #8c8590;
    --cliff-mid: #5f6656;
    --cliff-low: #4f5c45;
  }
  * { margin: 0; padding: 0; box-sizing: border-box; }
  html, body {
    width: 1200px; height: 900px; overflow: hidden;
    background: var(--page-bg);
  }
  .canvas { position: relative; width: 1200px; height: 900px; }
  .poster {
    position: absolute; top: 85px; width: 550px; height: 733px; overflow: hidden;
  }
  .poster--valley { left: 32px; }
  .poster--cliff { left: 614px; }
  .poster__photo { position: absolute; inset: 0; }
  .poster--valley .poster__photo {
    background: linear-gradient(170deg, var(--valley-top) 0%, var(--valley-mid) 50%, var(--valley-low) 100%);
  }
  .poster--cliff .poster__photo {
    background: linear-gradient(180deg, var(--cliff-top) 0%, var(--cliff-mid) 45%, var(--cliff-low) 100%);
  }
  .quote {
    position: absolute; left: 0; right: 0; text-align: center;
    font-family: "Bebas Neue", sans-serif; color: var(--quote-white);
    text-transform: uppercase;
  }
  .quote__line { display: block; }
  .poster--valley .quote { top: 42px; font-size: 93px; line-height: 105px; }
  .poster--cliff .quote { top: 32px; font-size: 78px; line-height: 95px; }
  .quote__author {
    position: absolute; left: 0; right: 0; text-align: center;
    font-family: "Bebas Neue", sans-serif; color: var(--quote-white);
    font-size: 32px; letter-spacing: 0.5px;
  }
  .poster--valley .quote__author { top: 570px; }
  .poster--cliff .quote__author { top: 597px; }
  .brand {
    position: absolute; right: 4px; bottom: 3px; width: 143px; height: 46px;
    background: var(--page-bg);
    display: flex; align-items: center; gap: 6px; padding: 0 6px;
  }
  .brand__dot {
    flex: none; width: 30px; height: 30px; border-radius: 50%;
    background: var(--brand-dot);
  }
  .brand__name {
    font-family: "Bebas Neue", sans-serif; color: var(--brand-ink);
    font-size: 14px; line-height: 14px;
  }
</style>
</head>
<body>
<main class="canvas">
  <section class="poster poster--valley">
    <div class="poster__photo" role="img" aria-label="Mountain valley with a winding switchback road, washed with a light haze"></div>
    <p class="quote">
      <span class="quote__line">Most</span>
      <span class="quote__line">Effective</span>
      <span class="quote__line">Way to</span>
      <span class="quote__line">Do it,</span>
      <span class="quote__line">Is to do it.</span>
    </p>
    <p class="quote__author">-ROSALIND PEMBERLY-</p>
    <div class="brand">
      <span class="brand__dot"></span>
      <span class="brand__name">Ridgeline Truck Driving School</span>
    </div>
  </section>

  <section class="poster poster--cliff">
    <div class="poster__photo" role="img" aria-label="Narrow cliffside jungle road with a truck and two vehicles, muted purple tint"></div>
    <p class="quote">
      <span class="quote__line">Start</span>
      <span class="quote__line">Where you are.</span>
      <span class="quote__line">Use</span>
      <span class="quote__line">What you have.</span>
      <span class="quote__line">Do</span>
      <span class="quote__line">What you can.</span>
    </p>
    <p class="quote__author">-DELMAR QUISBY-</p>
    <div class="brand">
      <span class="brand__dot"></span>
      <span class="brand__name">Ridgeline Truck Driving School</span>
    </div>
  </section>
</main>
</body>
</html>
```